Modern, clean and professional Wordpress design for a safety training company!

We are currently in the process of creating a new website for our business. We have hired a website developer and the main structure of our new Wordpress site is complete. We now need an overall design plan for the site. We need a very clean, professional and easy to follow website. Most of our website visitors only spend about 30-45 secs on our sites "shopping " so it is imperative that we have a strong Home Page.
Our company specializes in CPR and First Aid Certification Classes to businesses and individuals throughout Northern California. We provide these certifications two ways: ONSITE-We come to you, and HOSTED-we offer weekly classes at our 2 locations.
Our design needs to use the general green and blue colors of our logo. But we also like white.
The final design MUST communicate a legitimate, trustworthy and professional business. Our industry is VERY competitive and we need to STAND OUT.
Currently, the NEW website that we need a new design for is www.LifelineSkillsHub.com
Our old website is www.RescueCoursesBayview.com and we really do like the design of this website, but we just needed a Wordpress site for SEO purposes.
These are 3 websites that we really:
http://vorellamedica.com/
http://www.taldrix.com/
https://www.plumvey.com/
I have attached our Logo and other images if you need to use them but looking at the current two sites will be you best help.
Target Market(s)
1) Large businesses and industries that are looking for a company to provide ONSITE safety training classes at their office or place of work.
2) Individuals that need certifications for their jobs and other needs. These individuals are looking for a legitimate, trustworthy and professional environment to complete their training class.

```html
<!DOCTYPE html>
<html lang="en">
<head>
<meta charset="utf-8">
<title>Keystone Rescue Academy</title>
<link rel="stylesheet" href="https://fonts.googleapis.com/css2?family=Cinzel:wght@400;700&family=Arimo:wght@400;700&family=Open+Sans:wght@400;600&display=swap">
<style>
:root{
  --blue:#213b96;
  --navy:#1a2a7c;
  --deep:#142072;
  --footer:#2532a8;
  --footer-dark:#1a2388;
  --green:#8dc63f;
  --text:#333;
  --muted:#555;
  --line:#e3e3e3;
  --pale:#f5f7fa;
  --white:#fff;
}
*{box-sizing:border-box;margin:0;padding:0}
html,body{width:1200px;height:2476px;overflow:hidden;background:var(--white)}
body{font-family:"Arimo",Arial,sans-serif;color:var(--text);position:relative}
.abs{position:absolute}

/* header */
.brand{left:99px;top:40px;width:230px;font-family:"Cinzel",serif;font-weight:700;font-size:30px;line-height:1.05;color:var(--blue);text-align:center}
.contact{left:740px;top:52px;width:250px;font-family:"Cinzel",serif;font-size:17px;line-height:1.3;color:#222;text-align:right}
.phone{left:575px;top:106px;display:flex;align-items:center;gap:8px;font-family:"Open Sans",sans-serif;font-weight:600;font-size:21px;color:var(--blue);white-space:nowrap}
.email{left:740px;top:111px;width:250px;text-align:right;white-space:nowrap;font-family:"Cinzel",serif;font-size:14px;color:#222}
.badge{left:1012px;top:23px;width:80px;height:129px;background:var(--blue);border-radius:6px}

/* nav */
.nav{left:0;top:162px;width:1200px;height:43px;background:var(--blue)}
.nav ul{list-style:none;display:flex;position:absolute;left:99px;top:0;height:43px}
.nav li{height:43px;line-height:43px;padding:0 20px;font-size:14px;color:var(--white);text-transform:uppercase;white-space:nowrap}
.nav li.active{background:var(--green)}

/* hero */
.hero-side{left:0;top:205px;width:1200px;height:534px;background:linear-gradient(90deg,#9a9a9a,#d8d8d8 8%,#cfcfcf 92%,#8e8e8e)}
.hero-photo{left:99px;top:205px;width:1002px;height:534px;background:linear-gradient(135deg,#c9d6e6 0%,#8fa6cf 35%,#5a73b8 60%,#3d4f8f 100%)}
.tag{height:61px;line-height:61px;padding-left:38px;font-family:"Cinzel",serif;font-size:25px;color:var(--white);white-space:nowrap}
.tag-green{left:99px;top:503px;width:516px;background:var(--green)}
.tag-blue{left:99px;top:573px;width:635px;background:var(--blue)}
.tag-green em{font-style:normal;color:var(--navy)}
.tag-blue em{font-style:normal;color:var(--green)}

/* welcome */
.welcome{left:90px;top:765px;width:1020px;text-align:center}
.welcome h1{font-family:"Cinzel",serif;font-weight:400;font-size:34px;color:#222;margin-bottom:14px}
.welcome p{font-size:14.5px;line-height:1.45;color:#333;margin-bottom:16px}

/* pricing */
.plan{width:228px;border:1px solid var(--line);background:var(--white);text-align:center}
.plan .title{height:53px;line-height:56px;font-family:"Cinzel",serif;font-size:36px;color:#555}
.plan .price{height:82px;line-height:82px;background:var(--pale);font-family:"Open Sans",sans-serif;font-size:52px;color:var(--blue);border-top:1px solid var(--line);border-bottom:1px solid var(--line)}
.plan .feat{padding:18px 16px 0;height:162px;font-family:"Arimo",Arial,sans-serif;font-size:18px;color:#444}
.plan .feat li{list-style:none;padding:8px 0}
.plan .feat li.sep{height:1px;padding:0;background:var(--line);position:relative;margin:6px 0}
.plan .sep::after{content:"";position:absolute;left:50%;top:-4px;margin-left:-4px;width:8px;height:8px;background:#ccc;transform:rotate(45deg)}
.plan .btn{height:74px;line-height:74px;background:var(--blue);color:var(--white);font-family:"Arimo",Arial,sans-serif;font-size:21px}
.plan-featured{width:239px;background:var(--blue);border:none;color:var(--white)}
.plan-featured .flag{height:61px;line-height:64px;font-size:18px;letter-spacing:.5px}
.plan-featured .title{height:79px;line-height:79px;background:var(--navy);font-size:25px;color:var(--white)}
.plan-featured .price{background:var(--blue);border:none;color:var(--green);height:86px;line-height:96px}
.plan-featured .feat{color:var(--white);height:135px;padding-top:0}
.plan-featured .feat li{padding:7px 0}
.plan-featured .btn{background:var(--green);height:73px;line-height:73px}

/* featured */
.sec-title{font-family:"Cinzel",serif;font-size:32px;color:#222;font-weight:400}
.course{left:104px;width:520px;height:100px}
.course .thumb{position:absolute;left:0;top:0;width:158px;height:92px;border:4px solid #eee;background:linear-gradient(135deg,#8a95a8,#c3c8d2 50%,#6c7a94)}
.course h3{position:absolute;left:178px;top:2px;font-weight:400;font-size:16.5px;color:#222}
.course p{position:absolute;left:178px;top:28px;width:340px;font-size:13px;line-height:1.5;color:#444}
.more{color:var(--green);font-size:13px}
.event{left:698px;width:420px;height:110px}
.event .date{position:absolute;left:0;top:0;width:78px;height:78px;border-radius:50%;background:var(--blue);color:var(--white);text-align:center;border:3px solid #d5daf0}
.event .date b{display:block;font-size:19px;font-weight:400;padding-top:12px;border-bottom:1px solid rgba(255,255,255,.6);margin:0 12px;padding-bottom:4px}
.event .date span{font-size:12px;display:block;padding-top:5px}
.event h4{position:absolute;left:99px;top:0;font-family:"Cinzel",serif;font-weight:400;font-size:16px;color:var(--green);white-space:nowrap}
.event p{position:absolute;left:99px;top:24px;width:300px;font-family:"Open Sans",sans-serif;font-size:13px;line-height:1.35;color:#222}
.event .more{font-size:12px}

/* map */
.map{left:0;top:2021px;width:1200px;height:244px;background:linear-gradient(180deg,#e8e6df,#dcd9cf)}
.map-card{left:746px;top:2066px;width:353px;height:90px;background:var(--white);box-shadow:0 1px 4px rgba(0,0,0,.25);padding:12px 14px;font-size:13px;color:#333}
.map-card small{display:block;font-size:12px;color:#666;margin-top:4px}
.map-card .link{display:block;color:#3b6fd6;font-size:12px;margin-top:12px}
.map-card .acts{position:absolute;right:14px;top:14px;display:flex;gap:20px;font-size:12px;color:#3b6fd6;text-align:center}

/* footer */
.footer{left:0;top:2265px;width:1200px;height:157px;background:var(--footer);color:var(--white)}
.foot-h{font-size:13px;font-weight:700}
.news{width:190px;height:60px}
.news .pic{position:absolute;left:0;top:0;width:54px;height:54px;background:linear-gradient(135deg,#d9dce6,#9aa3bd);border:2px solid var(--white)}
.news .txt{position:absolute;left:68px;top:6px;font-size:9px;line-height:1.4;white-space:nowrap}
.news .txt b{display:block}
.news .date{position:absolute;left:2px;top:63px;font-size:8.5px;font-style:italic;white-space:nowrap}
.social{display:flex;gap:10px}
.social span{width:24px;height:24px;background:var(--footer-dark);border:1px solid rgba(255,255,255,.3)}
.loc{font-size:9.5px;line-height:1.6}
.foot-brand{left:855px;top:2300px;width:240px;font-family:"Cinzel",serif;font-weight:700;font-size:27px;line-height:1.1;text-align:center;color:var(--white)}
.copy{left:0;top:2422px;width:1200px;height:54px;line-height:54px;background:var(--footer-dark);color:var(--white);text-align:center;font-size:14px}
</style>
</head>
<body>

<header>
  <div class="abs brand">Keystone Rescue Academy</div>
  <div class="abs contact">480 Larkwood Ave Suite 12<br>Fairhollow, CA 95999</div>
  <div class="abs phone">
    <svg width="24" height="24" viewBox="0 0 24 24" aria-hidden="true"><circle cx="12" cy="12" r="11" fill="none" stroke="#8dc63f" stroke-width="2"/><path d="M8 6.5l2 2.5-1 1.5c.8 1.6 2 2.8 3.5 3.5l1.5-1 2.5 2-1 2c-4 0-8.5-4.5-8.5-8.5z" fill="#8dc63f"/></svg>
    555 014 2286
  </div>
  <div class="abs email">E-mail : info@kra-cpr.com</div>
  <div class="abs badge" role="img" aria-label="Accreditation badge"></div>
</header>

<nav class="abs nav">
  <ul>
    <li class="active">Home</li>
    <li>Class Calender</li>
    <li>Certification Classes</li>
    <li>Classes ofr Groups</li>
    <li>About Us</li>
    <li>Policies</li>
  </ul>
</nav>

<section>
  <div class="abs hero-side" role="img" aria-label="Greyscale photo of a training classroom"></div>
  <div class="abs hero-photo" role="img" aria-label="Photo of medical staff in blue scrubs working on a patient"></div>
  <div class="abs tag tag-green">Our company <em>specializes in</em></div>
  <div class="abs tag tag-blue">CPR and First Aid <em>certification classes</em></div>
</section>

<section class="abs welcome">
  <h1>Welcome to Keystone Rescue Academy!</h1>
  <p>Keystone Rescue Academy is Northern California's leader in CPR, BLS, and Basic First Aid Certifications! Taught by experienced Firefighters, our classes are much shorter and provide common sense knowledge and skills to each student to help prepare them for actual emergencies.</p>
  <p>By using real life emergency responders, we have revolutionized the standard, boring CPR class by teaching students the need-to-know information and preparing them with facts and tips to help them in true life and death situations!</p>
</section>

<section>
  <div class="abs plan" style="left:104px;top:1031px">
    <div class="title">CPR</div>
    <div class="price">$39</div>
    <ul class="feat"><li>Adult/ Child /Infant</li><li class="sep"></li><li>90 Minutes</li><li>No Book Fee</li></ul>
    <div class="btn">Register Now !</div>
  </div>
  <div class="abs plan" style="left:353px;top:1031px">
    <div class="title">BLS</div>
    <div class="price">$39</div>
    <ul class="feat"><li>Adult/ Child /Infant</li><li class="sep"></li><li>90 Minutes</li><li>No Book Fee</li></ul>
    <div class="btn">Register Now !</div>
  </div>
  <div class="abs plan plan-featured" style="left:596px;top:1003px">
    <div class="flag">MOST POPULAR</div>
    <div class="title">CPR + First Aid</div>
    <div class="price">$59</div>
    <ul class="feat"><li>Adult/ Child /Infant</li><li>90 Minutes</li><li>No Book Fee</li></ul>
    <div class="btn">Register Now !</div>
  </div>
  <div class="abs plan" style="left:853px;top:1038px">
    <div class="title">CPR</div>
    <div class="price">$39</div>
    <ul class="feat"><li>Adult/ Child /Infant</li><li class="sep"></li><li>90 Minutes</li><li>No Book Fee</li></ul>
    <div class="btn">Register Now !</div>
  </div>
</section>

<section>
  <h2 class="abs sec-title" style="left:99px;top:1518px">Featured Classses</h2>
  <div class="abs course" style="top:1584px">
    <div class="thumb" role="img" aria-label="Photo of a CPR practice session"></div>
    <h3>Theme Custom Colors Demo Video</h3>
    <p>Lorem ipsum dolor sit amet, consectetuer a iscing elit. Aenean commodo ligula eget dolo. Aenean massa. Cum sociis natoque penatibet<br><span class="more">Read more...</span></p>
  </div>
  <div class="abs course" style="top:1713px">
    <div class="thumb" role="img" aria-label="Photo of trainees practising on a manikin"></div>
    <h3>Theme Fonts Demo Video</h3>
    <p>Lorem ipsum dolor sit amet, consectetuer a iscing elit. Aenean commodo ligula eget dolo. Aenean massa. Cum sociis natoque penatibet<br><span class="more">Read more...</span></p>
  </div>
  <div class="abs course" style="top:1841px">
    <div class="thumb" role="img" aria-label="Photo of a classroom with training manikins"></div>
    <h3>Theme Custom Colors Demo Video</h3>
    <p>Lorem ipsum dolor sit amet, consectetuer a iscing elit. Aenean commodo ligula eget dolo. Aenean massa. Cum sociis natoque penatibet<br><span class="more">Read more...</span></p>
  </div>

  <h2 class="abs sec-title" style="left:703px;top:1520px">Featured Events</h2>
  <div class="abs event" style="top:1576px">
    <div class="date"><b>18.2</b><span>2015</span></div>
    <h4>Posuere erat a ante venenatis</h4>
    <p>Lorem ipsum dolor sit amet, consectetuer adipiscing elit. Nam leo lectus, molestie non, commodo id,dignissim sit amet,<br><span class="more">Read More</span></p>
  </div>
  <div class="abs event" style="top:1705px">
    <div class="date"><b>19.2</b><span>2015</span></div>
    <h4>Posuere erat a ante venenatis</h4>
    <p>Lorem ipsum dolor sit amet, consectetuer adipiscing elit. Nam leo lectus, molestie non, commodo id,dignissim sit amet,<br><span class="more">Read More</span></p>
  </div>
  <div class="abs event" style="top:1833px">
    <div class="date" style="background:var(--deep)"><b>20.2</b><span>2015</span></div>
    <h4>Posuere erat a ante venenatis</h4>
    <p>Lorem ipsum dolor sit amet, consectetuer adipiscing elit. Nam leo lectus, molestie non, commodo id,dignissim sit amet,<br><span class="more">Read More</span></p>
  </div>
</section>

<section>
  <div class="abs map" role="img" aria-label="Street map showing the training location"></div>
  <svg class="abs" style="left:556px;top:2185px" width="36" height="48" viewBox="0 0 36 48" aria-hidden="true"><path d="M18 2C9 2 3 9 3 17c0 11 15 27 15 27s15-16 15-27C33 9 27 2 18 2z" fill="#8dc63f"/><circle cx="18" cy="17" r="6" fill="#fff"/></svg>
  <div class="abs map-card">
    480 Larkwood Ave #12
    <small>Fairhollow, CA 95999</small>
    <span class="link">View larger map</span>
    <div class="acts"><span>Directions</span><span>Save</span></div>
  </div>
</section>

<footer>
  <div class="abs footer"></div>
  <div class="abs foot-h" style="left:165px;top:2280px;color:#fff">News</div>
  <div class="abs news" style="left:165px;top:2305px;color:#fff">
    <div class="pic" role="img" aria-label="News author photo"></div>
    <div class="txt"><b>LOREM IPSUM IS SIMPLY</b>Lorem Ipsum is simply<br>dummy text of the printing</div>
    <div class="date">Posted on 27 Jun 2013</div>
  </div>
  <div class="abs news" style="left:383px;top:2305px;color:#fff">
    <div class="pic" role="img" aria-label="News author photo"></div>
    <div class="txt"><b>LOREM IPSUM IS SIMPLY</b>Lorem Ipsum is simply<br>dummy text of the printing</div>
    <div class="date">Posted on 27 Jun 2013</div>
  </div>
  <div class="abs foot-h" style="left:607px;top:2280px;color:#fff">Connect</div>
  <div class="abs social" style="left:610px;top:2307px" aria-label="Social links"><span></span><span></span><span></span><span></span></div>
  <div class="abs foot-h" style="left:610px;top:2347px;color:#fff">Locations</div>
  <div class="abs loc" style="left:612px;top:2372px;color:#fff">
    <svg width="9" height="11" viewBox="0 0 9 12" aria-hidden="true"><path d="M4.5 0C2 0 0 2 0 4.5 0 7.5 4.5 12 4.5 12S9 7.5 9 4.5C9 2 7 0 4.5 0z" fill="#fff"/></svg>
    &nbsp;No : 12 , Street name, City, Country<br>&nbsp;&nbsp;&nbsp;&nbsp;Zip Code : 111111
  </div>
  <div class="abs foot-brand">Keystone Rescue Academy</div>
  <div class="abs copy">Copyright © 2014 Keystone Rescue Academy. All rights reserved.</div>
</footer>

</body>
</html>
```